Business Card Design Project

use presentation folder design and my logo and make 4 over 4 business cards

Industry/Entity Type

Business

Requirements
Must have
• use the design from my presentation folder and put my logo on it

Name
Title
phone
fax
email

```html
<!DOCTYPE html>
<html lang="en">
<head>
<meta charset="utf-8">
<title>Brightway Counseling Business Cards</title>
<link rel="stylesheet" href="https://fonts.googleapis.com/css2?family=Quicksand:wght@500;600;700&display=swap">
<style>
  :root {
    --bg: #ece8e3;
    --white: #ffffff;
    --grey: #8c8c8c;
    --grey-dark: #7a7a7a;
    --brown: #8a4a1f;
    --tan: #b08a6c;
    --tan-dark: #9c7a60;
    --beige: #c4b69c;
    --ink: #2a2a2a;
    --text-soft: #333333;
  }
  * { box-sizing: border-box; margin: 0; padding: 0; }
  html, body { width: 1200px; height: 1000px; overflow: hidden; }
  body {
    background: var(--bg);
    font-family: "Quicksand", sans-serif;
    position: relative;
  }
  .card {
    position: absolute;
    width: 740px;
    height: 478px;
    background: var(--white);
    overflow: hidden;
    box-shadow: 0 6px 14px rgba(0,0,0,0.25);
  }
  .card--front { left: 25px; top: 18px; }
  .card--back { left: 420px; top: 507px; }

  .brand {
    position: absolute;
    display: flex;
    flex-direction: column;
    align-items: center;
    color: var(--brown);
    font-weight: 600;
  }
  .brand__row { display: flex; align-items: center; gap: 14px; }
  .brand__dot { width: 34px; height: 34px; border-radius: 50%; background: var(--grey); }
  .brand__name { font-size: 54px; line-height: 1; letter-spacing: 0.5px; }
  .brand__sub { font-size: 20px; letter-spacing: 6px; margin-top: 4px; }
  .brand__tagline {
    font-size: 20px;
    letter-spacing: 1.5px;
    color: var(--ink);
    font-weight: 600;
    margin-top: 2px;
  }
  .card--front .brand { left: 0; right: 0; top: 118px; }

  .front__band {
    position: absolute;
    left: 0; right: 0; top: 250px; height: 240px;
    background: var(--tan);
    border-radius: 40px 40px 0 0;
  }
  .front__band--inner {
    top: 260px;
    background: var(--tan-dark);
  }
  .front__panel {
    position: absolute;
    left: 0; right: 0; top: 274px; bottom: 0;
    background: var(--grey);
    border-radius: 44px 44px 0 0;
    padding: 18px 20px 0 37px;
    color: var(--ink);
  }
  .person__name { font-size: 31px; font-weight: 600; letter-spacing: 0.5px; }
  .person__title { font-size: 19px; font-weight: 600; margin-top: 2px; }
  .contact {
    display: flex;
    margin-top: 16px;
    font-size: 15.5px;
    font-weight: 500;
    line-height: 20.5px;
    color: var(--text-soft);
  }
  .contact__list { display: grid; grid-template-columns: 86px auto; width: 393px; }
  .contact__office { flex: 1; }

  .back__pattern {
    position: absolute;
    inset: 0;
    background: linear-gradient(155deg,
      var(--beige) 0%,
      var(--grey-dark) 28%,
      var(--white) 44%,
      var(--white) 60%,
      var(--grey-dark) 76%,
      var(--brown) 100%);
  }
  .card--back .brand { left: 170px; top: 160px; }
</style>
</head>
<body>

<section class="card card--front">
  <div class="brand">
    <div class="brand__row">
      <span class="brand__dot"></span>
      <span class="brand__name">Brightway</span>
    </div>
    <span class="brand__sub">COUNSELING</span>
    <span class="brand__tagline">a fresh start recovery center</span>
  </div>

  <div class="front__band"></div>
  <div class="front__band front__band--inner"></div>
  <div class="front__panel">
    <h1 class="person__name">Darnell Whitaker</h1>
    <p class="person__title">Founder / CEO</p>
    <div class="contact">
      <div class="contact__list">
        <span>Phone</span><span>: 404.555.0182</span>
        <span>Fax</span><span>: 678.555.0147</span>
        <span>E-mail</span><span>: hello@brightwaycounsel.com</span>
      </div>
      <div class="contact__office">
        Corporate Office<br>
        418 Maple Ridge Rd. Suite 210<br>
        Marietta GA 30060
      </div>
    </div>
  </div>
</section>

<section class="card card--back">
  <div class="back__pattern" role="img" aria-label="Decorative background of tilted rounded tiles in grey, brown and beige"></div>
  <div class="brand">
    <div class="brand__row">
      <span class="brand__dot"></span>
      <span class="brand__name">Brightway</span>
    </div>
    <span class="brand__sub">COUNSELING</span>
    <span class="brand__tagline">a fresh start recovery center</span>
  </div>
</section>

</body>
</html>
```